Business Card Design

Need a new business card to represent our legal vertical focus. attached is an example of our old business card and newest logo. we would like the card to also identify "Legal Tech" as a tag line of business.

Our new address is
7381 Harrowgate Linden Rd.
Suite 418
Cincinnati, OH 45917

we no longer have a fax number.

Target Market(s)

Tech Consulting for Law Firms

Industry/Entity Type

Legal

Contact Information for Business Card

should use logo and colors. we are a b2b company

Other font styles liked:
• tahoma

Requirements
Must have
• all print should be in lower case just as shown in photos. tag line should not
Should not have
• pinstripes or drop shadows

```html
<!DOCTYPE html>
<html lang="en">
<head>
<meta charset="utf-8">
<title>Vantwell Legal Tech – Business Card</title>
<link rel="stylesheet" href="https://fonts.googleapis.com/css2?family=Noto+Sans:ital,wght@0,400;0,700;1,400&display=swap">
<style>
  :root {
    --navy: #053688;
    --orange: #e84e1b;
    --white: #ffffff;
    --stage: #2b2b2d;
    --ink: #0a3a8c;
  }
  * { box-sizing: border-box; margin: 0; padding: 0; }
  html, body { width: 1200px; height: 1000px; overflow: hidden; }
  body {
    background: var(--stage);
    font-family: "Noto Sans", Tahoma, sans-serif;
    display: flex;
    align-items: center;
    justify-content: center;
    gap: 70px;
  }
  .card {
    position: relative;
    width: 340px;
    height: 595px;
    background: var(--white);
    overflow: hidden;
  }

  /* front */
  .card-front .shapes { position: absolute; inset: 0; }
  .front-name {
    position: absolute; top: 22px; right: 24px;
    color: var(--white); font-weight: 700; font-size: 19px;
  }
  .wordmark {
    position: absolute; top: 280px; left: 0; right: 0;
    text-align: center;
  }
  .wordmark .brand {
    color: var(--navy); font-weight: 700; font-size: 50px; letter-spacing: -1px;
    line-height: 1;
  }
  .wordmark .tagline {
    color: var(--orange); font-size: 22px; letter-spacing: 1px; margin-top: 4px;
  }
  .front-url {
    position: absolute; bottom: 26px; right: 30px;
    color: var(--orange); font-size: 19px; letter-spacing: 2px;
  }

  /* back */
  .back-header {
    height: 118px; background: var(--navy);
    display: flex; align-items: center; justify-content: center;
  }
  .back-header .brand {
    color: var(--white); font-weight: 700; font-size: 56px; letter-spacing: -1px;
  }
  .identity { position: relative; margin-top: 34px; text-align: center; }
  .identity .rule {
    position: absolute; top: 16px; left: 0; right: 0; height: 2px; background: var(--orange);
  }
  .identity .name {
    position: relative; display: inline-block; background: var(--white);
    padding: 0 8px; font-weight: 700; font-size: 20px; color: var(--navy);
  }
  .identity .name .first { color: var(--orange); }
  .identity .title { font-style: italic; font-size: 15px; color: var(--navy); margin-top: 2px; }
  .contact {
    padding: 0 42px; margin-top: 58px; color: var(--ink); font-size: 17px; line-height: 1.3;
  }
  .contact p { margin-bottom: 42px; }
  .back-footer {
    position: absolute; bottom: 0; left: 0; right: 0; height: 80px; background: var(--orange);
  }
</style>
</head>
<body>

  <section class="card card-front" aria-label="card front">
    <svg class="shapes" width="340" height="595" viewBox="0 0 340 595" aria-hidden="true">
      <polygon points="0,0 340,0 340,190 0,250" fill="var(--navy)"/>
      <polygon points="0,420 0,595 22,595" fill="var(--navy)"/>
      <polygon points="340,380 300,400 245,595 340,595" fill="var(--navy)"/>
    </svg>
    <div class="front-name">martin l. oakes, jr.</div>
    <div class="wordmark">
      <div class="brand">Vantwell</div>
      <div class="tagline">Legal Tech</div>
    </div>
    <div class="front-url">vantwell.net</div>
  </section>

  <section class="card card-back" aria-label="card back">
    <header class="back-header"><span class="brand">Vantwell</span></header>
    <div class="identity">
      <div class="rule"></div>
      <div class="name"><span class="first">martin</span> l. oakes, jr.</div>
      <div class="title">president &amp; virtual cio</div>
    </div>
    <div class="contact">
      <p>moakes@vantwell.net</p>
      <p>513.555.0148</p>
      <p>7381 harrowgate linden rd.<br>suite 418<br>cincinnati, oh 45917</p>
    </div>
    <div class="back-footer"></div>
  </section>

</body>
</html>
```